Criação de Kit com 6 Layouts de Post para Redes Sociais (Facebook, Instagram e etc) + Capa de Facebook para Construção & Engenharia
" Atendemos principalmento sindicos de edificio "

```html
<!DOCTYPE html>
<html lang="pt-BR">
<head>
<meta charset="UTF-8">
<title>Dicas para uma Manutenção Predial Impecável</title>
<link rel="stylesheet" href="https://fonts.googleapis.com/css2?family=Montserrat:wght@800&family=Encode+Sans+Semi+Condensed:wght@500&family=Raleway:wght@600&display=swap">
<style>
  :root {
    --paper: #ffffff;
    --ink: #111111;
    --scaffold-yellow: #e9c21f;
    --scaffold-pale: #f3e7a6;
    --steel-grey: #b9b6ad;
    --worker-denim: #3a4763;
    --worker-shirt: #7a7c80;
    --tool-tan: #c8a25a;
    --brand-dark: #1b1b1b;
  }
  * { margin: 0; padding: 0; box-sizing: border-box; }
  html, body { width: 1200px; height: 1200px; overflow: hidden; background: var(--paper); }
  .post {
    position: relative;
    width: 1200px;
    height: 1200px;
    overflow: hidden;
    background: var(--paper);
  }
  .scaffold-backdrop {
    position: absolute;
    inset: 0;
    background:
      linear-gradient(160deg, var(--scaffold-pale) 0%, var(--scaffold-yellow) 22%, var(--steel-grey) 45%, rgba(255,255,255,0) 62%),
      linear-gradient(200deg, var(--scaffold-yellow) 0%, var(--steel-grey) 40%, rgba(255,255,255,0) 70%);
    opacity: .85;
  }
  .brush-sweep {
    position: absolute;
    inset: 0;
  }
  .worker-photo {
    position: absolute;
    left: 540px;
    top: 20px;
    width: 660px;
    height: 1180px;
    border-radius: 260px 260px 0 0;
    background: linear-gradient(180deg,
      var(--scaffold-yellow) 0%,
      #e3cfa0 18%,
      var(--worker-shirt) 34%,
      var(--worker-denim) 58%,
      var(--tool-tan) 88%,
      #a88545 100%);
    -webkit-mask-image: linear-gradient(90deg, transparent 0%, #000 14%, #000 100%);
    mask-image: linear-gradient(90deg, transparent 0%, #000 14%, #000 100%);
    opacity: .9;
  }
  .headline {
    position: absolute;
    left: 96px;
    top: 96px;
    font-family: "Montserrat", sans-serif;
    font-weight: 800;
    font-size: 100px;
    letter-spacing: 0;
    color: var(--ink);
    line-height: 1;
  }
  .subline {
    position: absolute;
    left: 96px;
    top: 268px;
    font-family: "Encode Sans Semi Condensed", sans-serif;
    font-weight: 500;
    font-size: 68px;
    line-height: 77px;
    color: var(--ink);
  }
  .brand {
    position: absolute;
    left: 40px;
    top: 756px;
    width: 500px;
    text-align: center;
    font-family: "Raleway", sans-serif;
    font-weight: 600;
    color: var(--brand-dark);
  }
  .brand-square {
    width: 164px;
    height: 164px;
    margin: 0 auto 30px;
    background: var(--brand-dark);
  }
  .brand-name {
    font-size: 62px;
    letter-spacing: 1px;
    line-height: 1;
  }
  .brand-field {
    margin-top: 18px;
    font-size: 26px;
    letter-spacing: 16px;
    padding-left: 16px;
  }
  .social-row {
    position: absolute;
    left: 200px;
    top: 1070px;
    display: flex;
    gap: 36px;
  }
  .social-dot {
    width: 32px;
    height: 32px;
    border-radius: 50%;
    background: var(--brand-dark);
  }
</style>
</head>
<body>
<main class="post">
  <div class="scaffold-backdrop" role="img" aria-label="Andaimes amarelos de uma obra em construção ao fundo"></div>

  <svg class="brush-sweep" width="1200" height="1200" viewBox="0 0 1200 1200" aria-hidden="true">
    <path d="M0 700 L1200 120 L1200 1200 L0 1200 Z" fill="#ffffff"/>
    <path d="M0 640 L1200 40 L1200 90 L0 690 Z" fill="#ffffff" opacity=".75"/>
    <path d="M0 220 L640 0 L900 0 L0 560 Z" fill="#ffffff" opacity=".55"/>
  </svg>

  <div class="worker-photo" role="img" aria-label="Foto de trabalhador sorridente de capacete amarelo, macacão azul e cinto de ferramentas, calçando luvas"></div>

  <h1 class="headline">DICAS</h1>
  <p class="subline">Para uma<br>Manutenção<br>Predial<br>Impecável!</p>

  <div class="brand">
    <div class="brand-square"></div>
    <div class="brand-name">R. VALADARES</div>
    <div class="brand-field">ENGENHARIA</div>
  </div>

  <div class="social-row" aria-label="Redes sociais">
    <span class="social-dot"></span>
    <span class="social-dot"></span>
    <span class="social-dot"></span>
  </div>
</main>
</body>
</html>
```